Design an Email Signature

I need an email signature to go at the bottom of my email account. I need it in an html format so the social media links can be hyperlinked.
I need the Logo and the following information incorporated.I will provide the correct information and hyperlinks once the contest is awarded. Please be creative with your design.

Mara Lusk
BRAVOKEN Corporate Wellness and Personal Training
Fitness Educator | Cycling Educator
000.000.0000
Email Address

Social Media icons hyperlinked.
Instagram Facebook Linkedin and Twitter

```html
<!DOCTYPE html>
<html lang="en">
<head>
<meta charset="utf-8">
<title>HTML Email Signature Design</title>
<link rel="stylesheet" href="https://fonts.googleapis.com/css2?family=Montserrat:wght@400;500;600;800&display=swap">
<style>
  :root {
    --board-pink: #f7a9a8;
    --ink: #2a2a2a;
    --card-white: #ffffff;
    --card-edge: #c9c9c9;
    --lime: #c8c65a;
    --lime-deep: #bdbb4c;
    --mark-dark: #231f20;
  }
  * { box-sizing: border-box; margin: 0; padding: 0; }
  html, body { width: 1200px; height: 823px; overflow: hidden; }
  body {
    background: var(--board-pink);
    font-family: "Montserrat", Arial, sans-serif;
    color: var(--ink);
    position: relative;
  }
  .board-title {
    position: absolute; top: 22px; left: 0; width: 1200px;
    text-align: center; font-weight: 800; font-size: 50px;
    letter-spacing: 3px; color: var(--ink); line-height: 1;
  }
  .signature {
    position: absolute; left: 51px; width: 1100px; height: 338px;
    background: var(--card-white); border: 1px solid var(--card-edge);
    overflow: hidden;
  }
  .signature--boxed { top: 93px; }
  .signature--icons { top: 453px; }
  .signature__band {
    position: absolute; left: 270px; right: 0; top: 98px; height: 180px;
    background: var(--lime);
  }
  .signature--icons .signature__band { top: 94px; }
  .brand-mark {
    position: absolute; left: 60px; top: 44px; width: 246px; height: 246px;
    background: var(--mark-dark); border: 5px solid var(--lime-deep);
    display: flex; align-items: center; justify-content: center;
  }
  .brand-mark__name {
    font-weight: 800; font-size: 30px; letter-spacing: 1px; color: var(--lime);
  }
  .person-name {
    position: absolute; left: 382px; top: 38px; height: 32px;
    padding: 0 6px; background: var(--lime);
    font-size: 27px; line-height: 32px; letter-spacing: 1px; font-weight: 400;
  }
  .signature--icons .person-name { top: 36px; }
  .person-name strong { font-weight: 600; }
  .person-role {
    position: absolute; left: 382px; top: 72px;
    font-size: 19.5px; line-height: 22px; font-weight: 500; letter-spacing: 0.4px;
  }
  .signature--icons .person-role { top: 68px; }
  .contact-line {
    position: absolute; left: 382px; display: flex; align-items: center; gap: 10px;
    font-size: 19px; line-height: 22px; font-weight: 500;
  }
  .contact-line--phone { top: 120px; }
  .contact-line--mail { top: 155px; }
  .signature--icons .contact-line--phone { top: 117px; }
  .signature--icons .contact-line--mail { top: 152px; }
  .contact-tag {
    width: 21px; height: 21px; border: 1.5px solid var(--ink);
    font-size: 14px; line-height: 18px; text-align: center; font-weight: 500;
  }
  .contact-icon { width: 22px; height: 22px; }
  .company-name {
    position: absolute; left: 382px; top: 203px;
    font-size: 21px; font-weight: 500; letter-spacing: 1.4px; line-height: 24px;
    text-transform: uppercase;
  }
  .signature--icons .company-name { top: 198px; }
  .social-links {
    position: absolute; left: 830px; top: 46px; display: flex; gap: 14px;
  }
  .signature--icons .social-links { top: 42px; }
  .social-links a { display: block; width: 40px; height: 40px; }
</style>
</head>
<body>
  <h1 class="board-title">HTML EMAIL SIGNATURE DESIGN</h1>

  <section class="signature signature--boxed">
    <div class="signature__band"></div>
    <div class="brand-mark"><span class="brand-mark__name">BRAVOKEN</span></div>
    <div class="person-name">MARA <strong>LUSK</strong></div>
    <div class="person-role">Fitness Educator | Cycling Educator</div>
    <div class="contact-line contact-line--phone"><span class="contact-tag">P</span>000.000.0000</div>
    <div class="contact-line contact-line--mail"><span class="contact-tag">M</span>yourmail@mailbox.com</div>
    <div class="company-name">Bravoken Corporate<br>Wellness and Personal Training</div>
    <nav class="social-links" aria-label="Social profiles">
      <a href="#" aria-label="Social profile 1"><svg viewBox="0 0 40 40"><circle cx="20" cy="20" r="17" fill="none" stroke="var(--lime-deep)" stroke-width="2"/></svg></a>
      <a href="#" aria-label="Social profile 2"><svg viewBox="0 0 40 40"><circle cx="20" cy="20" r="17" fill="none" stroke="var(--lime-deep)" stroke-width="2"/></svg></a>
      <a href="#" aria-label="Social profile 3"><svg viewBox="0 0 40 40"><circle cx="20" cy="20" r="17" fill="none" stroke="var(--lime-deep)" stroke-width="2"/></svg></a>
      <a href="#" aria-label="Social profile 4"><svg viewBox="0 0 40 40"><circle cx="20" cy="20" r="17" fill="none" stroke="var(--lime-deep)" stroke-width="2"/></svg></a>
    </nav>
  </section>

  <section class="signature signature--icons">
    <div class="signature__band"></div>
    <div class="brand-mark"><span class="brand-mark__name">BRAVOKEN</span></div>
    <div class="person-name">MARA <strong>LUSK</strong></div>
    <div class="person-role">Fitness Educator | Cycling Educator</div>
    <div class="contact-line contact-line--phone">
      <svg class="contact-icon" viewBox="0 0 22 22" aria-hidden="true"><rect x="1" y="1" width="20" height="20" fill="none" stroke="var(--ink)" stroke-width="1.5"/><path d="M5 9 Q11 4 17 9 L15 11 L13 9.5 L9 9.5 L7 11 Z" fill="none" stroke="var(--ink)" stroke-width="1.3"/><rect x="6" y="12" width="10" height="5" fill="none" stroke="var(--ink)" stroke-width="1.3"/></svg>
      000.000.0000
    </div>
    <div class="contact-line contact-line--mail">
      <svg class="contact-icon" viewBox="0 0 22 22" aria-hidden="true"><rect x="1" y="1" width="20" height="20" fill="none" stroke="var(--ink)" stroke-width="1.5"/><rect x="5" y="7" width="12" height="8" fill="none" stroke="var(--ink)" stroke-width="1.3"/><path d="M5 7 L11 12 L17 7" fill="none" stroke="var(--ink)" stroke-width="1.3"/></svg>
      yourmail@mailbox.com
    </div>
    <div class="company-name">Bravoken Corporate<br>Wellness and Personal Training</div>
    <nav class="social-links" aria-label="Social profiles">
      <a href="#" aria-label="Social profile 1"><svg viewBox="0 0 40 40"><circle cx="20" cy="20" r="17" fill="none" stroke="var(--lime-deep)" stroke-width="2"/></svg></a>
      <a href="#" aria-label="Social profile 2"><svg viewBox="0 0 40 40"><circle cx="20" cy="20" r="17" fill="none" stroke="var(--lime-deep)" stroke-width="2"/></svg></a>
      <a href="#" aria-label="Social profile 3"><svg viewBox="0 0 40 40"><circle cx="20" cy="20" r="17" fill="none" stroke="var(--lime-deep)" stroke-width="2"/></svg></a>
      <a href="#" aria-label="Social profile 4"><svg viewBox="0 0 40 40"><circle cx="20" cy="20" r="17" fill="none" stroke="var(--lime-deep)" stroke-width="2"/></svg></a>
    </nav>
  </section>
</body>
</html>
```